Business Card Design Project

We are looking to redesign the logo, business card and stationary of one of our group companies - KESTRAL SUPPLY COMPANY LLC.

The company specialises in industrial PVC and CPVC Piping systems. It is situated in the Middle East and the focus is purely in this region.

The logo work is already completed. The file is uploaded for the reference.

We are looking for a clean minimalistic design for the business card.

regards
Ormund
Updates

Hello Everyone!

Thanks for submitting your designs. 

Yet to find the right design. Probably the below links will give you guys some more idea on what we would like.

Minimalist design with some creativity.

Ormund

http://plaincardgallery.example/inspiration/15-beautifully-minimal-business-cards

http://www.quietlayouthub.example/2011/11/14/30-minimalist-business-card-design/

http://www.firmpixelnotes.example/inspiration/minimal-business-cards/

Target Market(s)

Industrial users

Industry/Entity Type

Industrial

Requirements
Must have
• - Minimalistic design

- Back side of the card should include the manufacturer BRAVOLINE CANADA's decal. The file is upload for the reference

- Further information
Company Name:
KESTRAL SUPPLY COMPANY LLC
Address:
PO Box 9087, Sharjah Industrial Area 5, Qutrani Road
Sharjah, United Arab Emirates
Telephone:
+971-6-5018-392
Fax:
+977-6-5018-393
Email:
mail@ksc-holding.example

- FYI, Kestral Supply Company LLC is the authorised distributor for BRAVOLINE CANADA in the UAE. For further information on bravoline please visit the website www.bravoline.example

```html
<!DOCTYPE html>
<html lang="en">
<head>
<meta charset="utf-8">
<title>Kestral Supply Company LLC — Business Card</title>
<link rel="stylesheet" href="https://fonts.googleapis.com/css2?family=Questrial&display=swap">
<style>
  :root {
    --page: #ffffff;
    --card: #231f20;
    --ink-light: #ffffff;
    --halftone: #bdbdbd;
    --rule: #e6e6e6;
  }
  html, body {
    margin: 0;
    padding: 0;
    width: 1200px;
    height: 900px;
    overflow: hidden;
    background: var(--page);
  }
  .canvas {
    position: relative;
    width: 1200px;
    height: 900px;
    font-family: "Questrial", "Helvetica Neue", Arial, sans-serif;
  }
  .card-shapes {
    position: absolute;
    inset: 0;
  }
  .brand-name {
    position: absolute;
    left: 620px;
    top: 168px;
    margin: 0;
    color: var(--ink-light);
    font-weight: 400;
    line-height: 1;
  }
  .brand-name .brand-main {
    display: block;
    font-size: 66px;
    letter-spacing: 3px;
  }
  .brand-name .brand-sub {
    display: block;
    margin-top: 10px;
    font-size: 19px;
    letter-spacing: 1.2px;
  }
  .contact-block {
    position: absolute;
    right: calc(1200px - 572px);
    top: 546px;
    margin: 0;
    color: var(--ink-light);
    font-style: normal;
    font-size: 19px;
    line-height: 22.5px;
    letter-spacing: 0.6px;
    text-align: right;
    text-transform: uppercase;
  }
  .contact-block .address { margin: 0 0 22px; }
  .contact-block .lines { margin: 0; }
</style>
</head>
<body>
<div class="canvas">
  <svg class="card-shapes" width="1200" height="900" viewBox="0 0 1200 900">
    <defs>
      <clipPath id="front-clip"><rect x="238" y="26" width="724" height="410"/></clipPath>
      <clipPath id="back-clip"><rect x="238" y="464" width="724" height="410"/></clipPath>
      <linearGradient id="halftone-front" x1="0" y1="0" x2="1" y2="0.3">
        <stop offset="0" stop-color="var(--halftone)" stop-opacity="0.85"/>
        <stop offset="0.55" stop-color="var(--halftone)" stop-opacity="0.25"/>
        <stop offset="0.8" stop-color="var(--halftone)" stop-opacity="0"/>
      </linearGradient>
      <linearGradient id="halftone-back" x1="0" y1="0.2" x2="1" y2="0">
        <stop offset="0" stop-color="var(--halftone)" stop-opacity="0.8"/>
        <stop offset="0.5" stop-color="var(--halftone)" stop-opacity="0.2"/>
        <stop offset="0.75" stop-color="var(--halftone)" stop-opacity="0"/>
      </linearGradient>
    </defs>

    <!-- front side -->
    <rect class="card-front" x="238" y="26" width="724" height="410" fill="var(--card)"/>
    <g clip-path="url(#front-clip)">
      <circle class="halftone-ring" cx="422" cy="272" r="170" fill="url(#halftone-front)"
              role="img" aria-label="Fading halftone dot crescent around the emblem circle"/>
      <circle class="emblem-disc" cx="442" cy="264" r="150" fill="var(--page)"/>
    </g>

    <!-- back side -->
    <rect class="card-back" x="238" y="464" width="724" height="410" fill="var(--card)"/>
    <g clip-path="url(#back-clip)">
      <circle class="halftone-ring" cx="944" cy="650" r="124" fill="url(#halftone-back)"
              role="img" aria-label="Fading halftone dot crescent around the half-circle cutout"/>
      <circle class="cutout-disc" cx="958" cy="644" r="102" fill="var(--page)"/>
    </g>
    <line class="divider" x1="602" y1="530" x2="602" y2="850" stroke="var(--rule)" stroke-width="2"/>
  </svg>

  <h1 class="brand-name">
    <span class="brand-main">KESTRAL</span>
    <span class="brand-sub">SUPPLY COMPANY LLC</span>
  </h1>

  <address class="contact-block">
    <p class="address">PO Box 9087<br>Sharjah Industrial<br>Area 5<br>Qutrani Road<br>Sharjah<br>United Arab Emirates</p>
    <p class="lines">P. +971.6.5018.392<br>F. +977.6.5018.393<br>mail@ksc-holding.example</p>
  </address>
</div>
</body>
</html>
```